Dufresne Roofing

Want a professional looking business card

Industry/Entity Type

Business

Contact Information for Business Card

Marc Dufresne ( Owner) marc@dufresneroofing-example.com, www.dufresneroofing-example.com, Adress: 4217 County road 42 Wendover,ON K0A3M1

```html
<!DOCTYPE html>
<html lang="en">
<head>
<meta charset="utf-8">
<title>Dufresne Roofing – Business Card</title>
<link rel="stylesheet" href="https://fonts.googleapis.com/css2?family=Montserrat:wght@400;500;600;700&display=swap">
<style>
  :root {
    --blue: #1f5fb8;
    --blue-deep: #174a94;
    --blue-light: #2b72d1;
    --white: #ffffff;
    --paper: #f2f3f4;
    --grey: #7c7f84;
    --grey-dark: #5f6166;
    --backdrop: #e6e7ea;
    --rule: rgba(255,255,255,0.45);
  }
  * { box-sizing: border-box; margin: 0; padding: 0; }
  html, body { width: 1200px; height: 780px; overflow: hidden; }
  body {
    background: var(--backdrop);
    font-family: "Montserrat", Arial, sans-serif;
    position: relative;
  }
  .card {
    position: absolute;
    top: 100px;
    width: 340px;
    height: 580px;
    border-radius: 4px;
    overflow: hidden;
    box-shadow: 0 10px 30px rgba(0,0,0,0.18);
  }
  .card--front { left: 210px; background: var(--paper); }
  .card--back {
    left: 650px;
    background: radial-gradient(circle at 50% 40%, var(--blue-light), var(--blue-deep) 90%);
  }

  /* front */
  .front-panel { position: absolute; left: 0; top: 0; width: 340px; height: 580px; }
  .brand {
    position: absolute; left: 0; right: 0; top: 88px;
    display: flex; align-items: center; justify-content: center; gap: 10px;
  }
  .brand__mark { width: 16px; height: 16px; background: var(--blue); }
  .brand__name {
    font-weight: 700; font-size: 24px; letter-spacing: 1px;
    text-transform: uppercase; color: var(--blue);
  }
  .card--back .brand { top: 300px; }
  .card--back .brand__mark { background: var(--white); }
  .card--back .brand__name { color: var(--white); }

  .contact {
    position: absolute; left: 0; right: 0; top: 262px;
    text-align: center; color: var(--white);
  }
  .contact__name {
    font-weight: 700; font-size: 22px; text-transform: uppercase; letter-spacing: 0.5px;
  }
  .contact__role { font-size: 14px; font-weight: 500; margin-top: 2px; }
  .contact__icon {
    display: block; margin: 14px auto 6px; width: 22px; height: 22px;
  }
  .contact__line { font-size: 14.5px; font-weight: 500; }
  .contact__line--small { font-size: 13px; }
  .contact__rule {
    width: 250px; height: 1px; background: var(--rule); margin: 10px auto 0;
  }
  .contact__address { font-size: 14.5px; font-weight: 500; line-height: 1.35; margin-top: 12px; }

  .site-band {
    position: absolute; left: 0; right: 0; bottom: 0; height: 62px;
    background: var(--grey);
    border-top: 4px solid #b9bcc0;
    display: flex; align-items: center; justify-content: center;
    color: var(--white); font-size: 13.5px; font-weight: 500; letter-spacing: 0.3px;
  }

  /* back */
  .hours {
    position: absolute; left: 0; right: 0; top: 360px;
    text-align: center; color: var(--white); font-size: 14.5px; line-height: 1.5;
  }
  .hours__day { font-weight: 700; }
</style>
</head>
<body>

<section class="card card--front" aria-label="Business card front">
  <svg class="front-panel" viewBox="0 0 340 580" aria-hidden="true">
    <defs>
      <linearGradient id="front-blue" x1="0" y1="0" x2="0" y2="1">
        <stop offset="0" stop-color="#2b72d1"/>
        <stop offset="1" stop-color="#1a54a6"/>
      </linearGradient>
    </defs>
    <polygon points="0,242 170,196 340,242 340,580 0,580" fill="url(#front-blue)"/>
  </svg>

  <div class="brand">
    <span class="brand__mark"></span>
    <span class="brand__name">Dufresne Roofing</span>
  </div>

  <div class="contact">
    <p class="contact__name">Marc Dufresne</p>
    <p class="contact__role">Owner</p>

    <svg class="contact__icon" viewBox="0 0 22 22" aria-hidden="true">
      <circle cx="11" cy="11" r="11" fill="#ffffff"/>
      <path d="M7.5 6.5c.6-.4 1.3-.3 1.6.3l.9 1.6c.3.5.1 1.1-.3 1.4l-.6.4c.6 1.3 1.6 2.3 2.9 2.9l.4-.6c.3-.5.9-.6 1.4-.3l1.6.9c.6.3.7 1 .3 1.6l-.6.8c-.5.6-1.3.8-2 .5-3-1.2-5.3-3.5-6.5-6.5-.3-.7-.1-1.5.5-2z" fill="#1f5fb8"/>
    </svg>
    <p class="contact__line">(613) 555-0142</p>
    <div class="contact__rule"></div>

    <svg class="contact__icon" viewBox="0 0 22 22" aria-hidden="true">
      <circle cx="11" cy="11" r="11" fill="#ffffff"/>
      <rect x="5.5" y="7" width="11" height="8" rx="1" fill="#1f5fb8"/>
      <path d="M5.8 7.4 11 11.5l5.2-4.1" fill="none" stroke="#ffffff" stroke-width="1"/>
    </svg>
    <p class="contact__line contact__line--small">marc@dufresneroofing-example.com</p>
    <div class="contact__rule"></div>

    <p class="contact__address">4217 County road 42<br>Wendover, ON K0A3M1</p>
  </div>

  <div class="site-band">www.dufresneroofing-example.com</div>
</section>

<section class="card card--back" aria-label="Business card back">
  <div class="brand">
    <span class="brand__mark"></span>
    <span class="brand__name">Dufresne Roofing</span>
  </div>

  <div class="hours">
    <p><span class="hours__day">Monday - Friday</span> : 9am - 5pm</p>
    <p><span class="hours__day">Saturday</span> : By appointment</p>
    <p><span class="hours__day">Sunday</span> : Closed</p>
  </div>

  <div class="site-band">www.dufresneroofing-example.com</div>
</section>

</body>
</html>
```